Looking for a creative label design for our retail coffee bags

We are a coffee manufacturer (coffee roaster) looking to re-brand our retail label for our coffee bags. Our main coffee blend that we sell is our Harborline Velvet Blend. You can use this name when creating the label. We are going for a look that represents our company as a coffee roaster. Please reference our website (www.brindlemugworks.com) and our Facebook page to learn more about our company and to give you more inspiration on creating this design.

Target Market(s)

Retail customers/grocery stores

Industry/Entity Type

Manufacturer

Requirements
Must have
• The size of the label has to be 3" width x 4" height

Logo must be Black
Nice to have
• We currently incorporate a color on our labels for each blend. For example, Harborline Velvet Blend (royal blue), Decaffeinated Blend (red), Breakfast Blend (green), Flavored coffees (gold).

Rustic/vintage style

```html
<!DOCTYPE html>
<html lang="en">
<head>
<meta charset="utf-8">
<title>Harborline Velvet Blend – Retail Label</title>
<link href="https://fonts.googleapis.com/css2?family=Oswald:wght@500;600&family=Playfair+Display:wght@800&family=Yellowtail&display=swap" rel="stylesheet">
<style>
  :root {
    --page: #eef0f2;
    --frame-red: #f50d0d;
    --navy: #0c1c3d;
    --navy-leaf: #1b2c52;
    --white: #ffffff;
    --ink: #000000;
  }
  * { margin: 0; padding: 0; box-sizing: border-box; }
  html, body {
    width: 1200px; height: 1200px; overflow: hidden;
    background: var(--page);
  }
  .label {
    position: absolute; left: 225px; top: 100px;
    width: 750px; height: 1000px;
    background: var(--frame-red);
    box-shadow: 8px 10px 18px rgba(0,0,0,0.25);
    overflow: hidden;
  }
  .label-field {
    position: absolute; inset: 20px;
    background: linear-gradient(160deg, var(--navy-leaf) 0%, var(--navy) 45%, var(--navy-leaf) 100%);
  }
  .brand-badge {
    position: absolute; left: 302px; top: 62px;
    width: 148px; height: 148px; border-radius: 50%;
    background: var(--white);
    display: flex; align-items: center; justify-content: center;
    text-align: center;
    font-family: "Oswald", sans-serif; font-weight: 500;
    font-size: 22px; line-height: 1.1; letter-spacing: 1px;
    color: var(--ink); text-transform: uppercase;
  }
  .script-rules { position: absolute; left: 0; top: 0; width: 750px; height: 1000px; }
  .blend-script {
    position: absolute; left: 40px; top: 372px; width: 670px;
    text-align: center; white-space: nowrap;
    font-family: "Yellowtail", cursive; font-size: 128px; line-height: 1;
    color: var(--frame-red);
    transform: rotate(-9deg);
  }
  .blend-variant, .blend-word {
    position: absolute; left: 345px; width: 270px; text-align: center;
    font-family: "Playfair Display", serif; font-weight: 800;
    color: var(--white);
  }
  .blend-variant { top: 518px; font-size: 38px; line-height: 1; letter-spacing: 10px; }
  .blend-word { top: 568px; font-size: 34px; line-height: 1; letter-spacing: 24px; }
  .flourish {
    position: absolute; width: 80px; height: 8px; border-radius: 4px;
    background: var(--white);
  }
  .flourish-left { left: 262px; top: 548px; }
  .flourish-right { left: 614px; top: 540px; }
  .site-url {
    position: absolute; left: 151px; top: 724px; width: 330px;
    font-family: "Oswald", sans-serif; font-weight: 600; white-space: nowrap;
    font-size: 16px; letter-spacing: 4.4px; color: var(--white);
  }
  .freshness-seal {
    position: absolute; left: 151px; top: 762px;
    width: 253px; height: 71px; background: var(--white);
  }
  .info-list {
    position: absolute; left: 510px; top: 724px; list-style: none;
    font-family: "Oswald", sans-serif; font-weight: 500;
    font-size: 12px; letter-spacing: 2.5px; line-height: 23.7px;
    color: var(--white);
  }
  .info-list li::before { content: "•"; margin-right: 7px; }
  .net-weight {
    position: absolute; left: 0; top: 898px; width: 750px;
    text-align: center;
    font-family: "Oswald", sans-serif; font-weight: 600;
    font-size: 20px; letter-spacing: 14px; color: var(--white);
  }
</style>
</head>
<body>
  <main class="label">
    <div class="label-field" role="img" aria-label="Navy background with a faint pattern of coffee leaves and cherries"></div>

    <div class="brand-badge">Brindle<br>Mugworks</div>

    <svg class="script-rules" viewBox="0 0 750 1000" aria-hidden="true">
      <path d="M286 322 L694 277" stroke="var(--frame-red)" stroke-width="7" fill="none" stroke-linecap="round"/>
      <path d="M106 560 Q420 505 731 448" stroke="var(--frame-red)" stroke-width="7" fill="none" stroke-linecap="round"/>
    </svg>

    <div class="blend-script">Harborline</div>

    <span class="flourish flourish-left" role="img" aria-label="Decorative swirl"></span>
    <div class="blend-variant">VELVET</div>
    <span class="flourish flourish-right" role="img" aria-label="Decorative swirl"></span>
    <div class="blend-word">BLEND</div>

    <div class="site-url">WWW.BRINDLEMUGWORKS.COM</div>
    <div class="freshness-seal" role="img" aria-label="Freshness seal badge"></div>
    <ul class="info-list">
      <li>INFOS HERE</li>
      <li>INFOS HERE</li>
      <li>INFOS HERE</li>
      <li>INFOS HERE</li>
      <li>INFOS HERE</li>
    </ul>

    <div class="net-weight">NET WEIGHT | 340 GRAMS</div>
  </main>
</body>
</html>
```